依頼詳細
新しく名刺を作ります。ARでスマホ等でスキャンすると動画が流せる企画物の名刺です。
ARでスキャンするマーカにする為にいくつか制約があります。以下の物使用しないで下さい。
グラデーションの物 (文字・背景にグラデーションがある物)
パターン柄の物 (水玉模様・唐草模様)
背景と文字・オブジェクトの色の境目が曖昧な物 (スキャンする際モノクロで判断するため、境目がはっきりしない物)
記載項目
Velmarisk
代表取締役
樫井 朋正 Tomomasa Kashii
kashii@velmarisk-mail.jp
090-5172-3948
株式会社ヴェルマリスク
本社 〒319-0587
栃木県足利市川辺町742-5
Tel 0284-57-3061
Fax 0284-57-3069
工場 栃木県足利市川辺町1864-9
希望イメージ
シンプル 複雑
単色 カラフル
暗い 明るい
日常 高級
遊び心 厳粛
未来的 伝統的
女性的 男性的
希望する色
緑系、黄・オレンジ系
納品ファイル
• イラストレーター形式 (.ai)
補足説明
ロゴは添付されているファイルを使用して下さい。
当選作品は内容の修正・変更をする場合があります。
■ 選んだ理由

弊社のイメージに合っているものを選びました。
シンプルかつ高級感を感じられるデザインが良いと思いました。

■ 提案者全員のお礼・コメント

すばらしいご提案ありがとうございました。

```html
<!DOCTYPE html>
<html lang="ja">
<head>
<meta charset="utf-8">
<title>Velmarisk 名刺 グリーンパターン</title>
<link href="https://fonts.googleapis.com/css2?family=Noto+Sans+JP:wght@400;500;700&family=Montserrat:wght@800&display=swap" rel="stylesheet">
<style>
  :root {
    --green: #2f9a3e;
    --green-dark: #237a30;
    --ink: #333333;
    --muted: #777777;
    --rule: #d6d6d6;
    --paper: #ffffff;
    --sheet: #ffffff;
  }
  * { margin: 0; padding: 0; box-sizing: border-box; }
  html, body { width: 893px; height: 1200px; overflow: hidden; background: var(--sheet); }
  body { position: relative; font-family: "Noto Sans JP", sans-serif; color: var(--ink); }

  .sheet-title { position: absolute; left: 54px; top: 250px; font-size: 20px; }
  .side-label { position: absolute; top: 308px; font-size: 19px; }
  .side-label.front { left: 54px; }
  .side-label.back { left: 476px; }

  .card { position: absolute; top: 363px; width: 384px; height: 792px; overflow: hidden; }
  .card-front { left: 54px; background: var(--paper); border: 1px solid var(--rule); }
  .card-back { left: 476px; background: var(--green); color: #fff; }

  .brand { position: absolute; left: 0; width: 100%; text-align: center; }
  .brand-mark { position: absolute; left: 50%; border-radius: 50%; transform: translateX(-50%); }
  .brand-name { font-family: "Montserrat", sans-serif; font-weight: 800; }

  .card-front .brand-mark { top: 82px; width: 58px; height: 58px; background: var(--green); }
  .card-front .brand-name { position: absolute; top: 170px; left: 0; width: 100%; font-size: 42px; color: var(--green); }

  .person { position: absolute; left: 52px; top: 330px; }
  .person .role { font-size: 15px; }
  .person .name { font-size: 38px; font-weight: 500; letter-spacing: 4px; line-height: 1.2; }
  .person .name-en { position: absolute; right: -138px; top: 84px; font-size: 12px; color: var(--muted); }
  .contact { position: absolute; left: 52px; top: 440px; font-size: 15px; line-height: 1.6; color: var(--green); font-weight: 500; }

  .chevron { position: absolute; left: 0; top: 500px; }

  .company { position: absolute; left: 0; top: 648px; width: 100%; text-align: center; font-size: 20px; font-weight: 500; }
  .address-band { position: absolute; left: 0; bottom: 0; width: 100%; height: 100px; background: var(--green); color: #fff; padding: 14px 0 0 26px; font-size: 11.5px; line-height: 1.75; }

  .card-back .brand-mark { top: 70px; width: 70px; height: 70px; background: #fff; }
  .card-back .brand-name { position: absolute; top: 172px; left: 0; width: 100%; font-size: 50px; color: #fff; }
  .tagline { position: absolute; left: 0; top: 300px; width: 100%; text-align: center; font-size: 14.5px; line-height: 2.4; }
  .url { position: absolute; right: 40px; top: 578px; font-size: 14px; letter-spacing: 0.5px; }
</style>
</head>
<body>
  <p class="sheet-title">グリーンパターン</p>
  <p class="side-label front">表面</p>
  <p class="side-label back">裏面</p>

  <section class="card card-front" aria-label="名刺 表面">
    <div class="brand">
      <span class="brand-mark"></span>
      <span class="brand-name">Velmarisk</span>
    </div>

    <div class="person">
      <p class="role">代表取締役</p>
      <p class="name">樫井 朋正</p>
      <p class="name-en">Tomomasa Kashii</p>
    </div>
    <div class="contact">
      <p>Mail：kashii@velmarisk-mail.jp</p>
      <p>Phone：090-5172-3948</p>
    </div>

    <svg class="chevron" width="384" height="150" viewBox="0 0 384 150" aria-hidden="true">
      <polyline points="0,0 192,48 384,0" fill="none" stroke="#cfcfcf" stroke-width="2"/>
      <polygon points="0,30 192,78 384,30 384,120 192,150 0,120" fill="#2f9a3e"/>
    </svg>

    <p class="company">株式会社ヴェルマリスク</p>
    <div class="address-band">
      <p>【本社】〒319-0587 栃木県足利市川辺町742-5</p>
      <p>Tel：0284-57-3061　Fax：0284-57-3069</p>
      <p>【工場】栃木県足利市川辺町1864-9</p>
    </div>
  </section>

  <section class="card card-back" aria-label="名刺 裏面">
    <div class="brand">
      <span class="brand-mark"></span>
      <span class="brand-name">Velmarisk</span>
    </div>
    <p class="tagline">お客様目線で、ホールの究極の望みを<br>満たしてまいります。</p>
    <p class="url">http://www.velmarisk.co.jp/</p>
  </section>
</body>
</html>
```